Australian Based Booking Platform Needs Playful Home Page & Profile Page To Showcase Our Acti...

COMPANY OVERVIEW:
WAVELOOP TRIPS is an Australian based activity booking platform. Our point of difference is our Kiosk machines that are located in hotels around Australia and allow customers instant access to book activities from the hotel reception.

HOME PAGE:
This page needs to clearly show that we are Australia’s leading booking platform.
Our Competition: https://www.roamquill.com.au/en
IMPORTANT SECTIONS ON THE HOME PAGE:
- Key Bullet Points (Best Price Guaranteed, Trusted By Thousands, Australian Owned, Unbeatable Support)
- Top Experiences – (Images of selected experiences in a slider format)
- Take Me There – Gold Coast, Carins, Port Duglas, Sunshine Coast, Whitsundays, Brisbane, Sydney, Adelaide, Hobart, Perth
- Top Deals For You – (Images of selected experiences in a slider format)
- Experiences You’ll Love – (Categories of Adventure Tours, Outdoor Activities, Hot Deals, Fun & Games, Zoos & Aquariums, Reef & Island Cruises)
- Testimonials – (some sort of slider format)
- Top New Experience – (Images of selected experiences in a slider format)
- Footer Menu
NOTE: Including some sort of mascot on the page to introduce a personality would be amazing. A Kangaroo or Koala could be a good choice.

REGION PAGE:
This page needs to clearly show what is on offer in the region. The layout of this page will be used for all regions in Australia (eg Gold Coast, Carins, Port Duglas, Sunshine Coast, Whitsundays, Brisbane, Sydney, Adelaide, Hobart, Perth)
IMPORTANT SECTIONS ON THE REGION PAGE:
- Categories: Adventure Tours, Outdoor Activities, Hot Deals, Fun & Games, Zoos & Aquariums, Reef & Island Cruises
o This Categories menu allows you to flick between sliders with activities from the different categories
- Footer Menu

PROFILE PAGE:
The layout of this page is going to be used to clearly show off every activity people can book.
Competitors Example:
https://www.trekvanta.com/tours/Sydney/Sydney-Harbour-Northern-beaches-and-National-Park/d357-137441P2
https://www.roamquill.com.au/en/gold-coast/pelwin-isle-dolphin-and-marrabin-reef-snorkelling-cruise
IMPORTANT SECTIONS ON THE PROFILE PAGE:
- Tour Title
- Photos / Video
- Booking Calanda (As displayed on the above link)
- Highlights & Inclusions
- Overview
- Location (Map)
- What To Bring
- Additional Information
- Booking Information
- Reviews:
- Terms & Conditions
NOTE: This page is to be displayed on a kiosk with the following dimensions;
- 1209.8mm x 680.4mm
- Aspect Ratio 16:9

I have uploaded some images of Australia, as well as our logo. Please feel free to use or not use these images as you decide.

Keep up the good work on the designs :)

Target Market(s)

Australian Holiday Makers

Industry/Entity Type

Tourism Booking Platform

Number of Pages Required

3 page

Font styles to use
Sans Serif

Requirements
Must have
• - This booking calendar https://app.clipvessel.com/fFoAUeq8Hhpn4
Nice to have
• A mascot or something to add character to the page.

```html
<!DOCTYPE html>
<html lang="en">
<head>
<meta charset="utf-8">
<title>Waveloop Trips – Home</title>
<link href="https://fonts.googleapis.com/css2?family=Open+Sans:wght@400;600;700;800&display=swap" rel="stylesheet">
<style>
:root{
  --orange:#f7b54a;
  --orange-deep:#e08f2c;
  --ink:#231f20;
  --text:#3a3a3a;
  --grey-bg:#f4f4f4;
  --white:#ffffff;
  --seller:#1f8a3a;
}
*{box-sizing:border-box;margin:0;padding:0}
html,body{width:1200px;height:3878px;overflow:hidden}
body{font-family:"Open Sans",Arial,sans-serif;color:var(--ink);background:var(--white);position:relative}
.abs{position:absolute}
.logo{font-weight:800;font-size:24px;letter-spacing:1px;color:var(--ink);white-space:nowrap}

/* navigation */
.nav{position:absolute;left:0;top:0;width:1200px;height:81px;background:var(--white);z-index:3}
.nav .logo{position:absolute;left:105px;top:22px}
.nav-link{position:absolute;top:30px;font-size:15px;color:var(--ink)}
.nav-link::after{content:"";display:inline-block;width:5px;height:5px;border-right:1.5px solid var(--ink);border-bottom:1.5px solid var(--ink);transform:rotate(45deg);margin-left:6px;position:relative;top:-3px}
.btn-outline{position:absolute;border:1.5px solid var(--ink);border-radius:16px;font-size:12px;display:flex;align-items:center;justify-content:center;color:var(--ink);background:var(--white);white-space:nowrap}
.btn-fill{position:absolute;background:var(--orange);border-radius:16px;font-size:12px;font-weight:600;color:var(--white);display:flex;align-items:center;justify-content:center;white-space:nowrap}

/* hero */
.hero-photo{position:absolute;left:0;top:81px;width:1200px;height:493px;
  background:
    radial-gradient(ellipse 260px 200px at 900px 140px,rgba(232,150,40,.85),rgba(232,150,40,0) 70%),
    radial-gradient(ellipse 200px 160px at 880px 110px,rgba(40,40,40,.55),rgba(40,40,40,0) 70%),
    linear-gradient(180deg,#8cbbe6 0%,#a9cdea 18%,#5f8a4e 42%,#4a6f3a 70%,#7d7f6e 100%)}
.hero-blob{position:absolute;left:0;top:81px}
.hero-title{position:absolute;left:105px;top:182px;font-size:41px;font-weight:700;line-height:50px;color:var(--ink)}
.hero-copy{position:absolute;left:105px;top:308px;width:350px;font-size:12px;line-height:16px;color:var(--ink)}
.hero-btn{left:105px;top:391px;width:175px;height:31px;background:transparent;font-weight:600}

.grey{position:absolute;left:0;background:var(--grey-bg);width:1200px}
.feature{position:absolute;top:624px;display:flex;align-items:center;gap:12px;font-size:19px;font-weight:700;color:var(--ink);white-space:nowrap}

.section-title{position:absolute;left:0;width:1200px;text-align:center;font-size:25px;font-weight:700;color:var(--ink)}
.rule{position:absolute;left:552px;width:96px;height:3px;background:var(--orange)}

.tab{position:absolute;top:843px;width:80px;height:27px;border:1.5px solid var(--ink);border-radius:5px;font-size:10px;display:flex;align-items:center;justify-content:center;background:var(--white)}
.tab.active{background:var(--orange);border-color:var(--orange);color:var(--white);font-weight:600}

/* mascot area: soft warm tones where the kangaroo character sits */
.mascot{position:absolute;background:
  radial-gradient(ellipse 38% 22% at 55% 20%,#f4bd6a 0%,#e9a04a 70%,rgba(233,160,74,0) 100%),
  radial-gradient(ellipse 30% 30% at 55% 55%,#fbe3bd 0%,#f0b462 60%,rgba(240,180,98,0) 100%),
  radial-gradient(ellipse 48% 46% at 50% 55%,#eaa24c 0%,#d98a2e 65%,rgba(217,138,46,0) 100%)}

/* deal card */
.deal{position:absolute;width:384px;height:175px;background:var(--white);border-radius:12px;box-shadow:0 2px 8px rgba(0,0,0,.05);z-index:2}
.deal .pic{position:absolute;left:5px;top:5px;width:150px;height:165px;border-radius:10px}
.deal .badges{position:absolute;left:12px;top:12px;display:flex;gap:4px}
.badge{font-size:6px;color:var(--white);padding:2px 6px;border-radius:3px;font-weight:600;white-space:nowrap}
.badge.seller{background:var(--seller)}
.badge.hot{background:var(--orange)}
.deal h3{position:absolute;left:170px;top:20px;font-size:15px;font-weight:700}
.deal p{position:absolute;left:170px;top:48px;width:200px;font-size:10.5px;line-height:15px;color:var(--text)}
.stars{color:var(--orange);letter-spacing:3px;font-size:16px;line-height:1}
.deal .stars{position:absolute;left:170px;top:110px}
.deal .price{position:absolute;left:170px;top:138px;font-size:10px;color:var(--ink)}
.price .was{color:var(--orange);margin-left:6px}

/* photo tones */
.ph-jetboat{background:
  radial-gradient(ellipse 30% 16% at 45% 62%,#d3242a 0%,#d3242a 50%,rgba(211,36,42,0) 100%),
  radial-gradient(ellipse 70% 30% at 55% 55%,#ffffff 0%,rgba(255,255,255,.6) 50%,rgba(255,255,255,0) 100%),
  linear-gradient(180deg,#9fcfe0 0%,#4aa6bf 30%,#2c8ba6 100%)}
.ph-surf{background:
  linear-gradient(180deg,#7fb5de 0%,#9cc6e6 35%,#3a73b8 50%,#2e6fb3 62%,#d9c9a3 72%,#cdb891 100%)}
.ph-birds{background:
  radial-gradient(ellipse 30% 40% at 55% 40%,#e8c3a3 0%,#d8a886 55%,rgba(216,168,134,0) 100%),
  radial-gradient(ellipse 40% 20% at 40% 78%,#d9432a 0%,#3a8a3a 60%,rgba(58,138,58,0) 100%),
  linear-gradient(160deg,#2f5a3a,#5a7f45 60%,#3d5f2f)}
.ph-slide{background:linear-gradient(135deg,#f3b232 0%,#f3b232 30%,#2f5c9f 45%,#f3b232 60%,#e8a020 100%)}

.round-arrow{position:absolute;border-radius:50%;background:var(--orange);display:flex;align-items:center;justify-content:center;z-index:2}

/* experiences */
.exp-pic{position:absolute;top:2571px;width:302px;height:223px;border-radius:4px}
.exp-title{position:absolute;top:2806px;font-size:19px;font-weight:600;color:var(--ink);white-space:nowrap}
.exp-copy{position:absolute;top:2849px;width:262px;font-size:10.5px;line-height:15px;color:var(--text)}
.exp-btn{top:2922px;width:108px;height:30px}

/* testimonials */
.review{position:absolute;top:3176px;width:253px;height:255px;border:1.5px solid #a9a9a9;border-radius:30px;background:var(--white);z-index:2}
.review .avatar{position:absolute;left:30px;top:20px;width:64px;height:64px;border-radius:50%;background:linear-gradient(160deg,#dce6ea,#7f98a3 60%,#3d5a66)}
.review .stars{position:absolute;left:30px;top:109px;font-size:19px}
.review p{position:absolute;left:30px;top:143px;width:195px;font-size:10.5px;line-height:15px;color:var(--text)}
.review .name{position:absolute;left:30px;top:220px;font-size:13px;font-weight:600}

/* footer */
.footer{position:absolute;left:0;top:3572px;width:1200px;height:306px;background:var(--ink);color:var(--white)}
.contact{position:absolute;left:138px;display:flex;align-items:center;gap:12px;font-size:12px}
.contact .dot{width:18px;height:18px;border-radius:50%;background:var(--orange);display:flex;align-items:center;justify-content:center}
.foot-links{position:absolute;top:81px;list-style:none;font-size:12px;line-height:24.5px}
.footer .logo{position:absolute;left:881px;top:86px;color:var(--white)}
.copyright{position:absolute;left:138px;top:245px;font-size:12px}
.social{position:absolute;top:230px;width:28px;height:28px;border-radius:50%;background:var(--orange)}
</style>
</head>
<body>

<header class="nav">
  <div class="logo">WAVELOOP TRIPS</div>
  <span class="nav-link" style="left:524px">Destinations</span>
  <span class="nav-link" style="left:676px">Experiences</span>
  <span class="nav-link" style="left:824px">Gifts</span>
  <span class="btn-outline" style="left:908px;top:27px;width:109px;height:29px">Login</span>
  <span class="btn-fill" style="left:1038px;top:27px;width:108px;height:29px">
    <svg width="10" height="12" viewBox="0 0 10 12" style="margin-right:6px"><path d="M5 0C6 3 9 4 9 8a4 4 0 0 1-8 0c0-2 1-3 2-4 0 2 1 3 2 3C5 5 4 3 5 0Z" fill="#fff"/></svg>Hot Deals
  </span>
</header>

<div class="hero-photo" role="img" aria-label="Photo of a looping orange roller coaster over treetops under blue sky"></div>
<svg class="hero-blob" width="700" height="520" viewBox="0 0 700 520">
  <path d="M0 0H615C645 95 590 195 480 290C380 380 300 470 135 505C75 516 30 502 0 482Z" fill="var(--orange)"/>
</svg>
<h1 class="hero-title">Experience the best<br>of Australia</h1>
<p class="hero-copy">Lorem ipsum dolor sit amet, consetetur sadipscing elitr, sed diam nonumy eirmod tempor invidunt ut labore et dolore magna aliquyam erat, sed diam voluptua.</p>
<span class="btn-outline hero-btn">See Whats On Offer</span>

<div class="grey" style="top:574px;height:842px"></div>

<svg class="abs" style="left:900px;top:650px" width="300" height="420" viewBox="900 650 300 420">
  <path d="M1200 655C1130 690 1075 760 1040 860C1015 945 1070 1030 1200 1058Z" fill="var(--ink)"/>
</svg>
<div class="mascot" role="img" aria-label="Cartoon kangaroo mascot leaping with a big smile" style="left:965px;top:680px;width:215px;height:290px"></div>

<div class="feature" style="left:52px">
  <svg width="24" height="24" viewBox="0 0 24 24"><path d="M3 12 12 3h9v9l-9 9Z" fill="var(--orange)"/><circle cx="16.5" cy="7.5" r="1.8" fill="#fff"/></svg>Best Price Guaranteed</div>
<div class="feature" style="left:352px">
  <svg width="28" height="24" viewBox="0 0 28 24"><circle cx="14" cy="12" r="10" fill="var(--orange)"/></svg>Australian Owned</div>
<div class="feature" style="left:612px">
  <svg width="26" height="26" viewBox="0 0 24 24"><path d="m12 2 3 6.5 7 .8-5.2 4.8 1.4 7L12 17.6 5.8 21l1.4-7L2 9.3l7-.8Z" fill="var(--orange)"/></svg>Trusted By Thousands</div>
<div class="feature" style="left:903px">
  <svg width="32" height="24" viewBox="0 0 32 24"><path d="M2 4c2 6 4 10 9 14v4H7C3 18 1 10 2 4Zm28 0c-2 6-4 10-9 14v4h4c4-4 6-12 5-18Z" fill="var(--orange)"/></svg>Unbeatable Support</div>

<h2 class="section-title" style="top:746px">Top experiences</h2>

<span class="tab active" style="left:370px">Gold Coast</span>
<span class="tab" style="left:465px">Carins</span>
<span class="tab" style="left:560px">Port Duglas</span>
<span class="tab" style="left:654px">Brisbane</span>
<span class="tab" style="left:748px">Sydney</span>

<article class="deal" style="left:200px;top:907px">
  <div class="pic ph-jetboat" role="img" aria-label="Photo of a red jet boat spinning across turquoise water"></div>
  <div class="badges"><span class="badge seller">Top Seller</span><span class="badge hot">Hot Deal</span></div>
  <h3>Lorum Ipsum</h3>
  <p>Lorem ipsum dolor sit amet, consetetur sadipscing elitr, sed diam nonumy eirmod tempor invidunt ut labore et dolore magna aliquyam erat, sed diam</p>
  <div class="stars">★★★★★</div>
  <div class="price">from &nbsp;$199.00<span class="was">$179.00</span></div>
</article>
<article class="deal" style="left:617px;top:907px">
  <div class="pic ph-surf" role="img" aria-label="Photo of surf students standing on boards on a sandy beach"></div>
  <div class="badges"><span class="badge seller">Top Seller</span><span class="badge hot">Hot Deal</span></div>
  <h3>Lorum Ipsum</h3>
  <p>Lorem ipsum dolor sit amet, consetetur sadipscing elitr, sed diam nonumy eirmod tempor invidunt ut labore et dolore magna aliquyam erat, sed diam</p>
  <div class="stars">★★★★★</div>
  <div class="price">from &nbsp;$199.00<span class="was">$179.00</span></div>
</article>
<article class="deal" style="left:200px;top:1107px">
  <div class="pic ph-birds" role="img" aria-label="Photo of a visitor feeding colourful lorikeets in a wildlife park"></div>
  <div class="badges"><span class="badge seller">Top Seller</span><span class="badge hot">Hot Deal</span></div>
  <h3>Lorum Ipsum</h3>
  <p>Lorem ipsum dolor sit amet, consetetur sadipscing elitr, sed diam nonumy eirmod tempor invidunt ut labore et dolore magna aliquyam erat, sed diam</p>
  <div class="stars">★★★★★</div>
  <div class="price">from &nbsp;$199.00<span class="was">$179.00</span></div>
</article>
<article class="deal" style="left:617px;top:1107px">
  <div class="pic ph-slide" role="img" aria-label="Photo of riders on a yellow and blue water slide"></div>
  <div class="badges"><span class="badge seller">Top Seller</span><span class="badge hot">Hot Deal</span></div>
  <h3>Lorum Ipsum</h3>
  <p>Lorem ipsum dolor sit amet, consetetur sadipscing elitr, sed diam nonumy eirmod tempor invidunt ut labore et dolore magna aliquyam erat, sed diam</p>
  <div class="stars">★★★★★</div>
  <div class="price">from &nbsp;$199.00<span class="was">$179.00</span></div>
</article>

<span class="btn-fill" style="left:560px;top:1321px;width:80px;height:27px;border-radius:4px;font-size:10px">View All</span>

<!-- Take me there -->
<h2 class="section-title" style="top:1469px">Take me there</h2>
<div class="rule" style="top:1515px"></div>
<div class="abs" role="img" aria-label="Photo of a river city skyline at sunset" style="left:164px;top:1596px;width:260px;height:226px;border-radius:14px 0 0 14px;background:linear-gradient(180deg,#f2c07a 0%,#e9b27a 25%,#8aa6b0 45%,#5f7f6a 60%,#3c6a7e 100%)"></div>
<div class="abs" role="img" aria-label="Photo of a coastal high-rise strip beside a long surf beach" style="left:770px;top:1596px;width:262px;height:226px;border-radius:0 14px 14px 0;background:linear-gradient(115deg,#5a92c8 0%,#8fa3b0 30%,#d9c9a0 45%,#ffffff 50%,#3a8fc0 58%,#1f6ea8 100%)"></div>
<div class="abs" role="img" aria-label="Photo of Sydney harbour with the opera house and city skyline" style="left:398px;top:1560px;width:397px;height:295px;border-radius:22px;background:
  radial-gradient(ellipse 28% 14% at 50% 62%,#f2efe8 0%,#d9d4c8 60%,rgba(217,212,200,0) 100%),
  linear-gradient(180deg,#8fb8e0 0%,#aac6e0 22%,#7f8f9b 38%,#4f7f5a 48%,#2a6a95 60%,#1f5f8a 100%);box-shadow:0 6px 16px rgba(0,0,0,.2)"></div>
<span class="abs" style="left:422px;top:1800px;font-size:25px;font-weight:700;color:var(--white)">Sydney</span>
<span class="round-arrow" style="left:140px;top:1684px;width:48px;height:48px"><svg width="14" height="14" viewBox="0 0 14 14"><path d="M9 2 4 7l5 5" stroke="#fff" stroke-width="2.2" fill="none"/></svg></span>
<span class="round-arrow" style="left:1008px;top:1684px;width:48px;height:48px"><svg width="14" height="14" viewBox="0 0 14 14"><path d="m5 2 5 5-5 5" stroke="#fff" stroke-width="2.2" fill="none"/></svg></span>

<!-- Top deals -->
<div class="grey" style="top:1930px;height:472px"></div>
<svg class="abs" style="left:0;top:1885px" width="400" height="540" viewBox="0 1885 400 540">
  <path d="M0 1890C120 1870 205 1920 262 2010C330 2120 392 2260 302 2360C232 2430 100 2422 0 2418Z" fill="var(--orange)"/>
</svg>
<div class="mascot" role="img" aria-label="Cartoon kangaroo mascot waving hello" style="left:0;top:1930px;width:330px;height:380px"></div>
<h2 class="section-title" style="top:1993px">Top deals for you</h2>
<div class="rule" style="top:2039px"></div>

<article class="deal" style="left:346px;top:2083px">
  <div class="pic ph-jetboat" role="img" aria-label="Photo of a red jet boat spinning across turquoise water"></div>
  <div class="badges"><span class="badge seller">Top Seller</span><span class="badge hot">Hot Deal</span></div>
  <h3>Lorum Ipsum</h3>
  <p>Lorem ipsum dolor sit amet, consetetur sadipscing elitr, sed diam nonumy eirmod tempor invidunt ut labore et dolore magna aliquyam erat, sed diam</p>
  <div class="stars">★★★★★</div>
  <div class="price">from &nbsp;$199.00<span class="was">$179.00</span></div>
</article>
<article class="deal" style="left:763px;top:2083px">
  <div class="pic ph-surf" role="img" aria-label="Photo of surf students standing on boards on a sandy beach"></div>
  <div class="badges"><span class="badge seller">Top Seller</span><span class="badge hot">Hot Deal</span></div>
  <h3>Lorum Ipsum</h3>
  <p>Lorem ipsum dolor sit amet, consetetur sadipscing elitr, sed diam nonumy eirmod tempor invidunt ut labore et dolore magna aliquyam erat, sed diam</p>
  <div class="stars">★★★★★</div>
  <div class="price">from &nbsp;$199.00<span class="was">$179.00</span></div>
</article>
<span class="round-arrow" style="left:1075px;top:2282px;width:33px;height:33px"><svg width="10" height="10" viewBox="0 0 14 14"><path d="M9 2 4 7l5 5" stroke="#fff" stroke-width="2.5" fill="none"/></svg></span>
<span class="round-arrow" style="left:1115px;top:2282px;width:33px;height:33px"><svg width="10" height="10" viewBox="0 0 14 14"><path d="m5 2 5 5-5 5" stroke="#fff" stroke-width="2.5" fill="none"/></svg></span>

<!-- Experiences you'll love -->
<h2 class="section-title" style="top:2471px">Experiences you'll love</h2>
<div class="rule" style="top:2517px"></div>
<span class="round-arrow" style="left:52px;top:2701px;width:33px;height:33px"><svg width="10" height="10" viewBox="0 0 14 14"><path d="M9 2 4 7l5 5" stroke="#fff" stroke-width="2.5" fill="none"/></svg></span>
<span class="round-arrow" style="left:1115px;top:2706px;width:33px;height:33px"><svg width="10" height="10" viewBox="0 0 14 14"><path d="m5 2 5 5-5 5" stroke="#fff" stroke-width="2.5" fill="none"/></svg></span>

<div class="exp-pic" role="img" aria-label="Photo of a family in cowboy hats with a dog at a ranch show" style="left:125px;background:
  radial-gradient(ellipse 40% 35% at 50% 55%,#c9a27a 0%,#9a6a45 60%,rgba(154,106,69,0) 100%),
  linear-gradient(160deg,#5a3a24,#8a5a36 50%,#3b2a1e)"></div>
<div class="exp-pic ph-jetboat" role="img" aria-label="Photo of a red jet boat carving across the water near a city skyline" style="left:450px"></div>
<div class="exp-pic" role="img" aria-label="Photo of a laughing rider on a yellow tube in a water slide" style="left:774px;background:
  radial-gradient(ellipse 45% 30% at 40% 85%,#f2c13a 0%,#f2c13a 55%,rgba(242,193,58,0) 100%),
  radial-gradient(ellipse 40% 35% at 85% 60%,#ffffff 0%,rgba(255,255,255,0) 100%),
  linear-gradient(160deg,#2d6fb2,#5fa6dc 50%,#8cc4ea)"></div>

<h3 class="exp-title" style="left:145px">Adventure Tours</h3>
<h3 class="exp-title" style="left:474px">Outdoor Activities</h3>
<h3 class="exp-title" style="left:793px">Hot Deals</h3>
<p class="exp-copy" style="left:145px">Lorem ipsum dolor sit amet, consetetur sadipscing elitr, sed diam nonumy eirmod tempor invidunt ut labore et dolore magna aliquyam erat, sed diam voluptua.</p>
<p class="exp-copy" style="left:472px">Lorem ipsum dolor sit amet, consetetur sadipscing elitr, sed diam nonumy eirmod tempor invidunt ut labore et dolore magna aliquyam erat, sed diam voluptua.</p>
<p class="exp-copy" style="left:793px">Lorem ipsum dolor sit amet, consetetur sadipscing elitr, sed diam nonumy eirmod tempor invidunt ut labore et dolore magna aliquyam erat, sed diam voluptua.</p>
<span class="btn-fill exp-btn" style="left:140px">View All</span>
<span class="btn-fill exp-btn" style="left:472px">View All</span>
<span class="btn-fill exp-btn" style="left:793px">View All</span>

<!-- Trusted by thousands -->
<svg class="abs" style="left:900px;top:2975px" width="300" height="545" viewBox="900 2975 300 545">
  <path d="M1200 2982C1110 3000 1030 3080 990 3180C950 3280 930 3400 1000 3470C1070 3520 1150 3512 1200 3502Z" fill="var(--orange)"/>
</svg>
<div class="mascot" role="img" aria-label="Cartoon kangaroo mascot hopping" style="left:915px;top:3050px;width:260px;height:400px"></div>

<h2 class="section-title" style="top:3079px">Trusted by thousands</h2>
<div class="rule" style="top:3125px"></div>

<article class="review" style="left:134px">
  <div class="avatar" role="img" aria-label="Reviewer portrait" style="background:linear-gradient(160deg,#9cc08a,#5a7f6a 60%,#3d5a66)"></div>
  <div class="stars">★★★★★</div>
  <p>Lorem ipsum dolor sit amet, consetetur sadipscing elitr, sed diam nonumy eirmod tempor invidunt ut labore et dolore magna aliquyam erat,</p>
  <div class="name">Jane Doe</div>
</article>
<article class="review" style="left:417px">
  <div class="avatar" role="img" aria-label="Reviewer portrait"></div>
  <div class="stars">★★★★★</div>
  <p>Lorem ipsum dolor sit amet, consetetur sadipscing elitr, sed diam nonumy eirmod tempor invidunt ut labore et dolore magna aliquyam erat,</p>
  <div class="name">Jane Doe</div>
</article>
<article class="review" style="left:700px">
  <div class="avatar" role="img" aria-label="Reviewer portrait"></div>
  <div class="stars">★★★★★</div>
  <p>Lorem ipsum dolor sit amet, consetetur sadipscing elitr, sed diam nonumy eirmod tempor invidunt ut labore et dolore magna aliquyam erat,</p>
  <div class="name">Jane Doe</div>
</article>

<footer class="footer">
  <div class="contact" style="top:79px"><span class="dot"><svg width="8" height="10" viewBox="0 0 8 10"><path d="M4 0a4 4 0 0 1 4 4c0 3-4 6-4 6S0 7 0 4a4 4 0 0 1 4-4Z" fill="#fff"/></svg></span>Address</div>
  <div class="contact" style="top:110px"><span class="dot"><svg width="9" height="9" viewBox="0 0 10 10"><path d="M2 0 4 2 3 4c1 1 2 2 3 3l2-1 2 2-2 2C4 10 0 6 0 2Z" fill="#fff"/></svg></span>+800 456 789</div>
  <div class="contact" style="top:140px"><span class="dot"><svg width="10" height="8" viewBox="0 0 10 8"><rect width="10" height="8" rx="1" fill="#fff"/><path d="m0 1 5 3 5-3" stroke="var(--orange)" fill="none"/></svg></span>info@waveloop-trips.com</div>

  <ul class="foot-links" style="left:452px"><li>Home</li><li>About Us</li><li>FAQs</li><li>Blog</li><li>Contact Us</li></ul>
  <ul class="foot-links" style="left:654px"><li>Privacy Policy</li><li>Terms &amp; Conditions</li><li>Cookie Policy</li></ul>

  <div class="logo">WAVELOOP TRIPS</div>
  <p class="copyright">Copyright 2023 Waveloop Trips. All Rights Reserved.</p>
  <span class="social" style="left:903px"></span>
  <span class="social" style="left:940px"></span>
  <span class="social" style="left:977px"></span>
  <span class="social" style="left:1014px"></span>
</footer>

</body>
</html>
```